Business Card Design Project

I am looking for a business card design for our online furniture company. Our company name is Tavrolen Goods, LLC. We sell exquisitely crafted high-end furniture and accessories tailored for a customer base with a wide range of design tastes. We encourage our customers to be creative when decorating the space in which they live and we should have a business card that is representative of that philosophy. A whimsical design is not off limits, but it should not have a look that can be off-putting to male customers. Professional single men are in the market for our products as well as women; therefore, we want a card that is equally appealing to both sexes.

Our card should be as unique as it is creative and should stand apart from typical and often bland business cards. In others words we looking for a card design that will elicit an interaction from other people to help them remember who we are. When a member of our team hands a potential customer our card, we want that person to feel as if they are holding a piece of art. We would like the card to be worthy of conversation unto itself. The card should be visually stimulating in such a way that it will be difficult for recipients to discard, even if they have electronically stored our business information. Keep in mind we will also be giving potential suppliers and interior designers alike our card so it needs to demonstrate that we are a serious and credible business. Both sides of the card can be used for the design if necessary. It may be beneficial for you to consult our website for further inspiration. Please do not hesitate to contact me with any questions you may have over the course of this project.

Industry/Entity Type

Business

Requirements
Must have
• Mirek Dunsby
Tavrolen Goods, LLC
Owner/Founder
mdunsby@tavrolengoods.example
555-284-9173
Shape Your Living Space (company slogan, if needed)
www.tavrolengoods.example

```html
<!DOCTYPE html>
<html lang="en">
<head>
<meta charset="utf-8">
<title>Tavrolen Goods — Business Card</title>
<link rel="stylesheet" href="https://fonts.googleapis.com/css2?family=Alegreya:ital,wght@0,400;1,700&family=Open+Sans:wght@400;600&display=swap">
<style>
  :root {
    --page: #ffffff;
    --wood-dark: #3a230f;
    --wood-mid: #6b4420;
    --wood-light: #8a5a2b;
    --ink: #141008;
    --cream: #ffffff;
    --band: #2e1a0a;
    --grain-line: rgba(40, 22, 8, 0.35);
  }
  * { margin: 0; padding: 0; box-sizing: border-box; }
  html, body { width: 1200px; height: 900px; overflow: hidden; background: var(--page); }
  .canvas { position: relative; width: 1200px; height: 900px; }

  .card {
    position: absolute;
    width: 600px;
    height: 380px;
    border-radius: 34px;
    overflow: hidden;
  }
  .card--front { left: 120px; top: 70px; }
  .card--back  { left: 480px; top: 470px; }

  .card__wood {
    position: absolute; inset: 0;
    background:
      radial-gradient(ellipse at 50% 45%, var(--wood-light) 0%, var(--wood-mid) 55%, var(--wood-dark) 100%);
  }
  .card__lines { position: absolute; inset: 0; }

  /* Front */
  .brand {
    position: absolute;
    left: 0; right: 0; top: 122px;
    text-align: center;
  }
  .brand__mark {
    width: 80px; height: 80px;
    margin: 0 auto 22px;
    background: var(--ink);
  }
  .brand__name {
    font-family: "Alegreya", Georgia, serif;
    font-weight: 400;
    font-size: 40px;
    letter-spacing: 5px;
    color: var(--ink);
    line-height: 1;
  }
  .brand__slogan {
    margin-top: 8px;
    font-family: "Alegreya", Georgia, serif;
    font-style: italic;
    font-weight: 700;
    font-size: 19px;
    letter-spacing: 2.5px;
    color: var(--cream);
  }

  /* Back */
  .card__band {
    position: absolute;
    left: 0; right: 0; top: 128px;
    height: 5px;
    background: var(--band);
  }
  .person {
    position: absolute;
    right: 42px; top: 46px;
    color: var(--cream);
    font-family: "Open Sans", Arial, sans-serif;
  }
  .person__name { font-size: 26px; font-weight: 600; line-height: 1.05; }
  .person__company, .person__role { font-size: 15px; line-height: 1.15; }

  .contact {
    position: absolute;
    left: 270px; top: 190px;
    list-style: none;
    color: var(--cream);
    font-family: "Open Sans", Arial, sans-serif;
    font-size: 15px;
  }
  .contact__item { display: flex; align-items: center; height: 34px; white-space: nowrap; }
  .contact__icon { width: 20px; height: 18px; margin-right: 22px; flex: none; }
</style>
</head>
<body>
<main class="canvas">

  <section class="card card--front" aria-label="Business card front">
    <div class="card__wood" role="img" aria-label="Dark walnut wood grain texture"></div>
    <svg class="card__lines" width="600" height="380" aria-hidden="true">
      <g stroke="var(--grain-line)" stroke-width="1.2">
        <line x1="40" y1="380" x2="420" y2="0"/>
        <line x1="200" y1="380" x2="580" y2="0"/>
        <line x1="0" y1="230" x2="230" y2="0"/>
      </g>
    </svg>
    <div class="brand">
      <div class="brand__mark"></div>
      <div class="brand__name">TavrolenGoods</div>
      <div class="brand__slogan">Shape Your Living Space</div>
    </div>
  </section>

  <section class="card card--back" aria-label="Business card back">
    <div class="card__wood" role="img" aria-label="Dark walnut wood grain texture"></div>
    <svg class="card__lines" width="600" height="380" aria-hidden="true">
      <g stroke="var(--grain-line)" stroke-width="1.2">
        <line x1="60" y1="380" x2="440" y2="0"/>
        <line x1="230" y1="380" x2="600" y2="10"/>
        <line x1="0" y1="250" x2="250" y2="0"/>
      </g>
    </svg>
    <div class="card__band"></div>

    <div class="person">
      <div class="person__name">Mirek Dunsby</div>
      <div class="person__company">Tavrolen Goods, LLC</div>
      <div class="person__role">Owner/Founder</div>
    </div>

    <ul class="contact">
      <li class="contact__item">
        <svg class="contact__icon" viewBox="0 0 20 18" aria-hidden="true">
          <rect x="1" y="3" width="18" height="12" fill="var(--cream)"/>
          <polyline points="1,3 10,10 19,3" fill="none" stroke="var(--wood-mid)" stroke-width="1.4"/>
        </svg>
        <span>mdunsby@tavrolengoods.example</span>
      </li>
      <li class="contact__item">
        <svg class="contact__icon" viewBox="0 0 20 18" aria-hidden="true">
          <path d="M1 6 Q10 0 19 6 L17 8 L14 6 L6 6 L3 8 Z" fill="var(--cream)"/>
          <rect x="4" y="8" width="12" height="9" rx="1" fill="var(--cream)"/>
          <circle cx="10" cy="12.5" r="2.4" fill="var(--wood-mid)"/>
        </svg>
        <span>555-284-9173</span>
      </li>
      <li class="contact__item">
        <svg class="contact__icon" viewBox="0 0 20 18" aria-hidden="true">
          <g fill="none" stroke="var(--cream)" stroke-width="1.2">
            <circle cx="10" cy="9" r="7.5"/>
            <ellipse cx="10" cy="9" rx="3.5" ry="7.5"/>
            <line x1="2.5" y1="9" x2="17.5" y2="9"/>
            <line x1="4" y1="5" x2="16" y2="5"/>
            <line x1="4" y1="13" x2="16" y2="13"/>
          </g>
        </svg>
        <span>www.tavrolengoods.example</span>
      </li>
    </ul>
  </section>

</main>
</body>
</html>
```